Business Card Design Project

We require a business card template to cover basic contact information - our company logo, names of employees, title, mobile and email.

Target Market(s)

Corporate

Industry/Entity Type

Business

Font styles to use
Sans Serif

Requirements
Nice to have
• Thinking it would be great just to have the logo taking up approximately half the space (so it goes as far across the top of the card as possible) and then contact details in the lower half of the card. Keen just to use only the two colours in the logo, on a white background.
Should not have
• No fussy drawings

```html
<!DOCTYPE html>
<html lang="en">
<head>
<meta charset="utf-8">
<title>Tidewell Developments – Business Card</title>
<link rel="stylesheet" href="https://fonts.googleapis.com/css2?family=Lexend:wght@300&display=swap">
<style>
  :root {
    --teal: #2e9fa8;
    --blue: #3462a3;
    --cream-light: #fffdf9;
    --cream: #fcf1e3;
    --ice: #dffbfd;
  }
  html, body {
    margin: 0;
    padding: 0;
    width: 1200px;
    height: 686px;
    overflow: hidden;
  }
  .card {
    position: relative;
    width: 1200px;
    height: 686px;
    font-family: "Lexend", sans-serif;
    font-weight: 300;
  }
  .brand-band {
    position: absolute;
    left: 0; top: 0;
    width: 1200px;
    height: 429px;
    background: radial-gradient(ellipse at 45% 85%, var(--cream-light) 0%, var(--cream) 70%);
  }
  .brand-name {
    position: absolute;
    left: 78px;
    top: 28px;
    margin: 0;
    font-size: 238px;
    line-height: 1;
    letter-spacing: -4px;
    color: var(--teal);
    font-weight: 300;
  }
  .brand-sub {
    position: absolute;
    right: 86px;
    top: 318px;
    margin: 0;
    font-size: 74px;
    line-height: 1;
    color: var(--teal);
    font-weight: 300;
  }
  .contact-band {
    position: absolute;
    left: 0; top: 429px;
    width: 1200px;
    height: 257px;
    background: var(--ice);
    color: var(--blue);
    font-size: 50px;
  }
  .contact-item {
    position: absolute;
    margin: 0;
    line-height: 1;
  }
  .employee-name  { left: 43px;  top: 44px; }
  .employee-title { left: 43px;  top: 141px; }
  .mobile         { right: 48px; top: 44px; }
  .email          { right: 48px; top: 141px; }
</style>
</head>
<body>
  <div class="card">
    <header class="brand-band">
      <p class="brand-name">Tidewell</p>
      <p class="brand-sub">developments</p>
    </header>
    <section class="contact-band">
      <p class="contact-item employee-name">Employee name</p>
      <p class="contact-item employee-title">Employee title</p>
      <p class="contact-item mobile">Mobile number</p>
      <p class="contact-item email">E-mail</p>
    </section>
  </div>
</body>
</html>
```